" LUMIVEX Somos uma Autoridade de Registro (AR) com autorização de funcionamento concedida pelo Governo Federal, responsável pelo recebimento, validação, encaminhamento de solicitações de emissão ou revogação de certificados digitais e identificação, de forma presencial, de seus solicitantes. Estamos entre as melhores do Brasil, fornecendo Certificados Digitais (cuja definição encontra-se em http://www.oquarel.org.br/certificacao-digital/o-que-e), além de projetos especiais, para garantir a autenticidade, a integridade e a validade jurídica de documentos em forma eletrônica, das aplicações de suporte e das aplicações habilitadas que utilizem certificados digitais, bem como a realização de transações eletrônicas seguras, através de nossos Pontos de Atendimentos com abrangência nacional. Os benefícios dos Certificados Digitais e onde usá-los: http://www.oquarel.org.br/certificacao-digital/beneficios A Lumivex atuando no mercado de identificação digital disponibiliza a seus clientes a nova geração de certificados digitais. São inovadores, simples, rápidos, confiáveis, seguros, práticos, e, sobretudo, fáceis de usar. A nova geração dos Certificados Digitais da Lumivex pode ser usado tanto no computador quanto no celular, smartphone e tablet. Possibilitando que você assine documentos eletrônicos, se identifique a partir de qualquer lugar de forma descomplicada ou acesse a portais do Governo (p.ex. Agência Tamboril, emissão de notas fiscais eletrônicas, processo judicial eletrônico, etc.). A Lumivex garante a autenticidade, sigilo, integridade, privacidade e total conveniência para você e para os seus negócios (sites, lojas virtuais e servidores web). "

```html
<!DOCTYPE html>
<html lang="pt-BR">
<head>
<meta charset="UTF-8">
<title>Lumivex — Cartão de Visita</title>
<link rel="stylesheet" href="https://fonts.googleapis.com/css2?family=Russo+One&family=Open+Sans:wght@400;600&display=swap">
<style>
  :root {
    --bg: #ececec;
    --card: #ffffff;
    --brand-blue: #1a2a9c;
    --brand-green: #2f9a2a;
    --brand-yellow: #f6c61b;
    --text: #333333;
    --muted: #666666;
  }
  * { box-sizing: border-box; margin: 0; padding: 0; }
  html, body { width: 1200px; height: 1200px; overflow: hidden; }
  body {
    background: var(--bg);
    position: relative;
    font-family: "Open Sans", sans-serif;
  }
  .card {
    position: absolute;
    left: 200px;
    width: 800px;
    height: 444px;
    background: var(--card);
    border-radius: 40px;
    overflow: hidden;
    box-shadow: 0 8px 24px rgba(0,0,0,0.12);
  }
  .card--front { top: 90px; }
  .card--back { top: 600px; }
  .card__accent {
    position: absolute;
    top: 0;
    right: 0;
    width: 160px;
    height: 100%;
    background: linear-gradient(90deg, var(--brand-green) 0%, var(--brand-blue) 65%, var(--brand-yellow) 100%);
  }

  .brand {
    position: absolute;
    left: 60px;
    top: 150px;
    display: flex;
    flex-direction: column;
    align-items: flex-start;
  }
  .brand__row { display: flex; align-items: center; gap: 16px; }
  .brand__mark { width: 54px; height: 54px; background: var(--brand-green); }
  .brand__name {
    font-family: "Russo One", sans-serif;
    font-size: 88px;
    line-height: 1;
    color: var(--brand-blue);
    letter-spacing: 2px;
  }
  .brand__tagline {
    margin-top: 10px;
    margin-left: 72px;
    font-family: "Russo One", sans-serif;
    font-size: 20px;
    letter-spacing: 8px;
    color: var(--brand-green);
  }

  .back-brand {
    position: absolute;
    left: 60px;
    top: 48px;
    display: flex;
    align-items: center;
    gap: 10px;
  }
  .back-brand .brand__mark { width: 26px; height: 26px; }
  .back-brand .brand__name { font-size: 40px; }
  .contacts {
    position: absolute;
    left: 66px;
    top: 140px;
    list-style: none;
    display: flex;
    flex-direction: column;
    gap: 16px;
  }
  .contacts li {
    display: flex;
    align-items: center;
    gap: 20px;
    font-size: 22px;
    color: var(--text);
  }
  .contacts svg { width: 22px; height: 22px; fill: none; stroke: var(--muted); stroke-width: 2; }
  .contacts .dot { width: 16px; height: 16px; margin: 0 3px; border-radius: 50%; background: var(--muted); }

  .palette {
    position: absolute;
    right: 60px;
    bottom: 50px;
    display: flex;
  }
  .palette span { width: 50px; height: 40px; }
  .swatch--yellow { background: var(--brand-yellow); }
  .swatch--blue { background: var(--brand-blue); }
  .swatch--green { background: var(--brand-green); }
</style>
</head>
<body>

  <section class="card card--front" aria-label="Frente do cartão">
    <div class="card__accent" role="img" aria-label="Faixa decorativa em verde, azul e amarelo"></div>
    <div class="brand">
      <div class="brand__row">
        <span class="brand__mark"></span>
        <span class="brand__name">LUMIVEX</span>
      </div>
      <span class="brand__tagline">CERTIFICADORA DIGITAL</span>
    </div>
  </section>

  <section class="card card--back" aria-label="Verso do cartão">
    <div class="card__accent" role="img" aria-label="Faixa decorativa em verde, azul e amarelo"></div>
    <div class="back-brand">
      <span class="brand__mark"></span>
      <span class="brand__name">LUMIVEX</span>
    </div>
    <ul class="contacts">
      <li>
        <svg viewBox="0 0 24 24"><path d="M5 3h4l2 5-3 2a12 12 0 0 0 6 6l2-3 5 2v4a2 2 0 0 1-2 2A18 18 0 0 1 3 5a2 2 0 0 1 2-2z"/></svg>
        (00) 0000-0000
      </li>
      <li>
        <svg viewBox="0 0 24 24"><rect x="7" y="2" width="10" height="20" rx="2"/><line x1="11" y1="18" x2="13" y2="18"/></svg>
        (00) 90000-0000
      </li>
      <li><span class="dot"></span>/lumivex</li>
      <li>
        <svg viewBox="0 0 24 24"><rect x="2" y="5" width="20" height="14" rx="1"/><path d="M2 6l10 7 10-7"/></svg>
        contato@lumivex.com.br
      </li>
      <li>
        <svg viewBox="0 0 24 24"><circle cx="12" cy="12" r="10"/><path d="M2 12h20M12 2c3 3 3 17 0 20M12 2c-3 3-3 17 0 20"/></svg>
        www.lumivex.com.br
      </li>
    </ul>
  </section>

  <div class="palette" aria-label="Paleta de cores">
    <span class="swatch--yellow"></span>
    <span class="swatch--blue"></span>
    <span class="swatch--green"></span>
  </div>

</body>
</html>
```